New Book Cover Design Project: Belly Balance and Calm Stomachs

5-1/2 x8-1/2 inch cover front and back, with spine for a 45,000-word book.
Title: Belly Balance and Calm Stomachs. Subtitle: Restore Your Inner Garden and Leave Behind Bloating Woes, Slow Energy, Mental Haze, Extra Pounds, and Swelling—for a Brighter, Lighter Self. Author: Mavis Thornquill. Thorough discussion of how to achieve good digestion and lifelong gut health mainly through a quality diet based on real food free of chemicals. Ten chapters. I am author of nine other books, focused on vibrant health through natural living. I'm looking for a simple and impactful cover. My most recent book, also with cover from Pixel Harbor, is The Lone Pantry Plan: Reshape Your Bond with Meals in Only 30 Days.

Target Market(s)

Mostly middle aged women who want to feel better and have real solutions for their digestion and gut problems, including less midriff fat

Industry/Entity Type

Self-help health information from a nutritionist and family health advocate.

Font styles to use
Serif

Colors

Designer to choose colors to be used in the design.

Requirements
Must have
• Some way to indicate the author is a woman, my name being Mavis Thornquill. Multicolored, upbeat, with some graphic reference to gut health but not with an illustration of microbes or intestinesnGra
Nice to have
• Perhaps an image of women's flat bellies or before and after images of flat bellies, or anything else suggestive of a smooth-functioning living systempas
Should not have
• See above.

```html
<!DOCTYPE html>
<html lang="en">
<head>
<meta charset="utf-8">
<title>Belly Balance and Calm Stomachs — Mavis Thornquill</title>
<link rel="stylesheet" href="https://fonts.googleapis.com/css2?family=Montserrat:ital,wght@0,600;0,700;1,500&display=swap">
<style>
  :root {
    --bg: #ebc3e3;
    --orange: #ff5004;
    --navy: #14387f;
    --band: #1e1c21;
    --band-text: #ebe8f0;
    --ink: #232126;
    --art-deep: #123f66;
    --art-mid: #3a8fae;
    --art-light: #e4e2e8;
  }
  * { margin: 0; padding: 0; box-sizing: border-box; }
  html, body { width: 800px; height: 1200px; overflow: hidden; background: var(--bg); }
  .cover {
    position: relative;
    width: 800px;
    height: 1200px;
    background: var(--bg);
    font-family: "Montserrat", sans-serif;
    overflow: hidden;
  }
  .title { position: absolute; left: 92px; top: 19px; }
  .title-line { display: block; font-weight: 700; white-space: nowrap; }
  .title-main {
    color: var(--orange);
    font-size: 162px;
    line-height: 166px;
    letter-spacing: -4px;
  }
  .title-sub {
    color: var(--navy);
    font-size: 98px;
    line-height: 95px;
    letter-spacing: -2px;
  }
  .title-sub.first { margin-top: 0; }
  .subtitle { position: absolute; left: 95px; top: 643px; list-style: none; }
  .subtitle li {
    display: block;
    width: 335px;
    height: 34px;
    margin-bottom: 13.5px;
    padding-left: 19px;
    background: var(--band);
    color: var(--band-text);
    font-style: italic;
    font-weight: 500;
    font-size: 18px;
    line-height: 34px;
    white-space: nowrap;
  }
  .hero-art {
    position: absolute;
    left: 430px;
    top: 522px;
    width: 370px;
    height: 678px;
  }
  .author {
    position: absolute;
    left: 102px;
    top: 1114px;
    color: var(--ink);
    font-weight: 600;
    font-size: 30px;
    letter-spacing: 0.3px;
    text-transform: uppercase;
    white-space: nowrap;
  }
</style>
</head>
<body>
  <main class="cover">
    <h1 class="title">
      <span class="title-line title-main">Belly</span>
      <span class="title-line title-main">Balance</span>
      <span class="title-line title-sub first">and Calm</span>
      <span class="title-line title-sub">Stomachs</span>
    </h1>

    <ul class="subtitle">
      <li>Restore Your Inner Garden and</li>
      <li>Leave Behind Bloating Woes,</li>
      <li>Slow Energy, Mental Haze,</li>
      <li>Extra Pounds, and</li>
      <li>Swelling—for a</li>
      <li>Brighter, Lighter</li>
      <li>Self</li>
    </ul>

    <svg class="hero-art" viewBox="0 0 370 678" role="img" aria-label="Paper-cut illustration: a layered teal body outline behind a white woman running">
      <defs>
        <linearGradient id="hero-fill" x1="0" y1="0" x2="1" y2="0">
          <stop offset="0" stop-color="var(--art-mid)"/>
          <stop offset="0.5" stop-color="var(--art-deep)"/>
          <stop offset="1" stop-color="var(--art-light)"/>
        </linearGradient>
      </defs>
      <rect x="0" y="0" width="370" height="678" fill="url(#hero-fill)" opacity="0.85"/>
    </svg>

    <p class="author">Mavis Thornquill</p>
  </main>
</body>
</html>
```